Discreet simple classy for adult entertainment

I would like a matte black business card with gold writing for my business. Keeping it simple. Having my following:

Lana frost
Events. Entertainment. Promotions
0491726580

or alternatively could have what i had on my previous card below but i think i prefer the above as again - discretion.

Maybe a nice gold line thru the card or some other very simple design . Or not open to ideas/ can be doublesided if any good ideas with that.

included pics of my old bus card. not sure weather i want a photo on it or not. if i do it wont be the same pic. i kinda wanted a card that was discreet so if it was in someones wallet they wouldn't neccessarily realise it was from a stripper.

Target Market(s)

men

Industry/Entity Type

Business

Contact Information for Business Card

Lana frost
0491726580

Requirements
Nice to have
• i don't know i am really open to anything. im giving my cards to guys so something they can have in their wallet that is discreet preferably.

```html
<!DOCTYPE html>
<html lang="en">
<head>
<meta charset="utf-8">
<title>Lana Frost — Business Card</title>
<link rel="stylesheet" href="https://fonts.googleapis.com/css2?family=Cinzel:wght@400&family=Source+Sans+3:wght@400&display=swap">
<style>
  :root {
    --backdrop: #ececec;
    --card-black: #121212;
    --emboss-black: #181818;
    --edge-red: #c3121b;
    --ink-white: #f2f2f2;
  }
  * { box-sizing: border-box; margin: 0; padding: 0; }
  html, body {
    width: 1200px;
    height: 900px;
    overflow: hidden;
    background: var(--backdrop);
  }
  .sheet {
    position: relative;
    width: 1200px;
    height: 900px;
  }
  .card {
    position: absolute;
    top: 297px;
    width: 500px;
    height: 306px;
    background: var(--card-black);
    border: 3px solid var(--edge-red);
  }
  .card--front { left: 75px; }
  .card--back { left: 625px; }

  .card__name {
    position: absolute;
    inset: 0;
    display: flex;
    align-items: center;
    justify-content: center;
    font-family: "Cinzel", serif;
    font-size: 30px;
    letter-spacing: 0.32em;
    padding-left: 0.32em;
    text-transform: uppercase;
    color: var(--emboss-black);
    text-shadow: 0 1px 0 #262626, 0 -1px 0 #050505;
  }

  .services {
    position: absolute;
    left: 0;
    right: 0;
    top: 128px;
    display: flex;
    justify-content: center;
    align-items: center;
    gap: 34px;
    font-family: "Source Sans 3", sans-serif;
    font-size: 15px;
    letter-spacing: 0.02em;
    color: var(--ink-white);
    list-style: none;
  }
  .services__divider {
    width: 1px;
    height: 14px;
    background: var(--edge-red);
  }
  .phone {
    position: absolute;
    left: 0;
    right: 0;
    top: 172px;
    text-align: center;
    font-family: "Source Sans 3", sans-serif;
    font-size: 15px;
    letter-spacing: 0.04em;
    color: var(--ink-white);
  }
</style>
</head>
<body>
  <main class="sheet">
    <section class="card card--front" aria-label="Card front">
      <h1 class="card__name">Lana Frost</h1>
    </section>

    <section class="card card--back" aria-label="Card back">
      <ul class="services">
        <li>Entertainment</li>
        <li class="services__divider" aria-hidden="true"></li>
        <li>Events</li>
        <li class="services__divider" aria-hidden="true"></li>
        <li>Promotions</li>
      </ul>
      <p class="phone">0491 726 580</p>
    </section>
  </main>
</body>
</html>
```